Business Card Design Project

for a second hand vintage clothing store. shop name is The Velvet Cupboard

Cards to be double sided

The name on the card is Joanna Whitfield

Information to put on card:

The Velvet Cupboard
Joanna Whitfield (no job title)
42/871 Dunmore St, Glenwick, Sydney, NSW, 2009.
Mobile: 0412 905 261
Email: thevelvetcupboard@mailbox.com.au
Web: www.thevelvetcupboard.com.au

Target Market(s)

Women looking at vintage clothing

Industry/Entity Type

Clothing

```html
<!DOCTYPE html>
<html lang="en">
<head>
<meta charset="utf-8">
<title>The Velvet Cupboard – Business Card</title>
<link rel="stylesheet" href="https://fonts.googleapis.com/css2?family=Arimo:wght@400;700&display=swap">
<style>
  :root {
    --backdrop: #f2ecd9;
    --maroon: #5c2a3b;
    --maroon-deep: #5a2236;
    --crimson: #b3241f;
    --cream: #efe2a6;
    --gold: #e3b85a;
    --white: #ffffff;
    --card-shadow: rgba(60, 30, 20, 0.28);
  }
  html, body {
    margin: 0;
    padding: 0;
    width: 1200px;
    height: 951px;
    overflow: hidden;
    background: var(--backdrop);
    font-family: "Arimo", Arial, sans-serif;
  }
  .canvas {
    position: relative;
    width: 1200px;
    height: 951px;
  }
  .card {
    position: absolute;
    width: 640px;
    height: 391px;
    border-radius: 26px;
    overflow: hidden;
    box-shadow: 0 8px 22px var(--card-shadow);
  }
  /* Front side */
  .card-front {
    left: 150px;
    top: 55px;
    background: var(--maroon);
    display: flex;
    align-items: center;
    justify-content: center;
  }
  .wordmark {
    margin: 0;
    color: var(--cream);
    font-family: "Arimo", Arial, sans-serif;
    font-weight: 400;
    letter-spacing: 1px;
    white-space: nowrap;
  }
  .card-front .wordmark { font-size: 52px; }

  /* Back side */
  .card-back {
    left: 410px;
    top: 500px;
    background: var(--white);
  }
  .back-band {
    position: absolute;
    left: 0; top: 0;
    width: 100%;
    height: 84%;
    background: radial-gradient(ellipse 60% 85% at 48% 42%, var(--crimson) 0%, #8a2230 55%, var(--maroon-deep) 100%);
  }
  .holder-name {
    position: absolute;
    left: 40px;
    top: 36px;
    margin: 0;
    font-size: 25px;
    font-weight: 400;
    color: var(--white);
  }
  .holder-name .first { color: var(--gold); }
  .contact-list {
    position: absolute;
    left: 342px;
    top: 118px;
    margin: 0;
    padding: 0;
    list-style: none;
    color: var(--white);
    font-size: 15px;
    line-height: 19px;
  }
  .contact-list li {
    position: relative;
    padding-left: 26px;
  }
  .contact-list .address { margin-bottom: 12px; }
  .contact-list svg {
    position: absolute;
    left: 0;
    top: 2px;
    width: 15px;
    height: 15px;
  }
  .card-back .wordmark {
    position: absolute;
    left: 40px;
    top: 238px;
    font-size: 40px;
  }
</style>
</head>
<body>
<main class="canvas">
  <section class="card card-front" aria-label="Card front">
    <h1 class="wordmark">The Velvet Cupboard</h1>
  </section>

  <section class="card card-back" aria-label="Card back">
    <div class="back-band"></div>
    <h2 class="holder-name"><span class="first">Joanna</span> Whitfield</h2>
    <ul class="contact-list">
      <li class="address">
        <svg viewBox="0 0 16 16" aria-hidden="true"><path d="M8 1 L15 8 H13 V15 H9.5 V10.5 H6.5 V15 H3 V8 H1 Z" fill="var(--cream)"/></svg>
        42/871 Dunmore St, Glenwick,<br>Sydney, NSW, 2009.
      </li>
      <li>
        <svg viewBox="0 0 16 16" aria-hidden="true"><rect x="4.5" y="1" width="7" height="14" rx="1.5" fill="var(--cream)"/><rect x="6" y="3" width="4" height="7" fill="var(--maroon-deep)"/></svg>
        0412 905 261
      </li>
      <li>
        <svg viewBox="0 0 16 16" aria-hidden="true"><rect x="1.5" y="3.5" width="13" height="9" rx="1" fill="var(--cream)"/><path d="M1.5 4 L8 9 L14.5 4" stroke="var(--maroon-deep)" stroke-width="1.2" fill="none"/></svg>
        thevelvetcupboard@mailbox.com.au
      </li>
      <li>
        <svg viewBox="0 0 16 16" aria-hidden="true"><circle cx="8" cy="8" r="6.5" fill="var(--cream)"/></svg>
        www.thevelvetcupboard.com.au
      </li>
    </ul>
    <p class="wordmark">The Velvet Cupboard</p>
  </section>
</main>
</body>
</html>
```